Creative Brief
Stationery and Cards
Need clean, simple, modern cards/letterhead
Simple
Dale Pruett
Executive Direstor
418 Hollister Avenue
Suite 500
New York, NY 10012
Dpruett@brimlow.com
www.mistvaleloft.com

```html
<!DOCTYPE html>
<html lang="en">
<head>
<meta charset="utf-8">
<title>Mistvale Stationery</title>
<link rel="stylesheet" href="https://fonts.googleapis.com/css2?family=Marcellus&family=Lato:wght@400;700&display=swap">
<style>
  :root {
    --paper: #ffffff;
    --stage: #ffffff;
    --frame: #d9d9d9;
    --ink: #3b3b3b;
    --ink-soft: #6a6a6a;
    --blue: #3fb4e5;
    --orange: #f4a93a;
    --green: #93c54b;
    --mark: #3fb4e5;
    --shadow: rgba(0, 0, 0, 0.28);
  }
  html, body {
    margin: 0;
    padding: 0;
    width: 1200px;
    height: 681px;
    overflow: hidden;
    background: var(--stage);
  }
  .canvas {
    position: relative;
    width: 1200px;
    height: 681px;
    background: var(--stage);
    font-family: "Lato", Arial, sans-serif;
    color: var(--ink);
  }
  .presentation-frame {
    position: absolute;
    left: 20px; top: 10px;
    width: 1158px; height: 659px;
    border: 1px solid var(--frame);
    box-sizing: border-box;
  }
  .piece {
    position: absolute;
    background: var(--paper);
    box-shadow: 3px 4px 8px var(--shadow);
  }
  .brand {
    position: absolute;
    display: flex;
    flex-direction: column;
    align-items: center;
  }
  .brand-dot {
    border-radius: 50%;
    background: var(--mark);
  }
  .brand-name {
    font-family: "Marcellus", Georgia, serif;
    color: var(--ink);
    letter-spacing: 0.04em;
    line-height: 1;
  }
  .rule-set {
    position: absolute;
    height: 3px;
  }
  .rule-set span {
    position: absolute;
    top: 0;
    height: 3px;
  }
  .rule-blue { background: var(--blue); }
  .rule-orange { background: var(--orange); }
  .rule-green { background: var(--green); }
  .contact {
    position: absolute;
    text-align: center;
    color: var(--ink-soft);
    line-height: 1.45;
    white-space: nowrap;
  }

  /* Envelope front */
  .envelope-front { left: 67px; top: 96px; width: 490px; height: 209px; }
  .envelope-front .brand { left: 52px; top: 24px; }
  .envelope-front .brand-dot { width: 40px; height: 40px; margin-bottom: 12px; }
  .envelope-front .brand-name { font-size: 27px; }
  .envelope-front .rule-set { left: 0; right: 0; top: 170px; }
  .envelope-front .contact { left: 0; right: 0; top: 180px; font-size: 8px; }

  /* Envelope back */
  .envelope-back { left: 67px; top: 312px; width: 490px; height: 276px; }
  .envelope-back .flap { position: absolute; left: 0; top: 0; }
  .envelope-back .brand { left: 225px; top: 78px; }
  .envelope-back .brand-dot { width: 40px; height: 40px; }

  /* Letterhead */
  .letterhead { left: 619px; top: 36px; width: 444px; height: 593px; }
  .letterhead .brand { left: 0; right: 0; top: 34px; }
  .letterhead .brand-dot { width: 40px; height: 40px; margin-bottom: 12px; }
  .letterhead .brand-name { font-size: 27px; }
  .letterhead .faint-mark {
    position: absolute;
    left: 114px; top: 216px;
    width: 216px; height: 216px;
    border-radius: 50%;
    background: radial-gradient(circle, rgba(63,180,229,0.08), rgba(147,197,75,0.06) 60%, rgba(244,169,58,0.05));
  }
  .letterhead .rule-set { left: 0; right: 0; top: 534px; }
  .letterhead .contact { left: 0; right: 0; top: 548px; font-size: 8px; }

  /* Business card front */
  .card-front { left: 967px; top: 132px; width: 216px; height: 113px; }
  .card-front .brand { left: 0; right: 0; top: 10px; }
  .card-front .brand-dot { width: 16px; height: 16px; margin-bottom: 6px; }
  .card-front .brand-name { font-size: 14px; }
  .card-front .holder { position: absolute; left: 0; right: 0; top: 54px; text-align: center; }
  .card-front .holder-name { font-size: 7px; font-weight: 700; color: var(--ink); }
  .card-front .holder-title { font-size: 5.5px; color: var(--ink-soft); }
  .card-front .rule-set { left: 0; right: 0; top: 80px; height: 2px; }
  .card-front .rule-set span { height: 2px; }
  .card-front .contact { left: 0; right: 0; top: 87px; font-size: 5px; }

  /* Business card back */
  .card-back { left: 967px; top: 269px; width: 216px; height: 110px; }
  .card-back .brand { left: 0; right: 0; top: 20px; }
  .card-back .brand-dot { width: 46px; height: 46px; margin-bottom: 8px; }
  .card-back .brand-name { font-size: 13px; }
</style>
</head>
<body>
<div class="canvas">
  <div class="presentation-frame"></div>

  <!-- Envelope front -->
  <section class="piece envelope-front">
    <div class="brand">
      <div class="brand-dot"></div>
      <div class="brand-name">MISTVALE</div>
    </div>
    <div class="rule-set">
      <span class="rule-blue" style="left:0;width:144px"></span>
      <span class="rule-orange" style="left:156px;width:168px"></span>
      <span class="rule-green" style="left:336px;width:154px"></span>
    </div>
    <div class="contact">
      418 Hollister Avenue | Suite 500 | New York, NY 10012<br>
      Cell: 917-555-0142 | Email: Dpruett@brimlow.com | www.mistvaleloft.com
    </div>
  </section>

  <!-- Envelope back -->
  <section class="piece envelope-back">
    <svg class="flap" width="490" height="276" viewBox="0 0 490 276" aria-hidden="true">
      <path d="M0 2 Q10 8 40 30 Q120 70 245 72 Q370 70 450 30 Q480 8 490 2" fill="none" stroke="#555" stroke-width="1"/>
    </svg>
    <div class="brand">
      <div class="brand-dot"></div>
    </div>
  </section>

  <!-- Letterhead -->
  <section class="piece letterhead">
    <div class="faint-mark"></div>
    <div class="brand">
      <div class="brand-dot"></div>
      <div class="brand-name">MISTVALE</div>
    </div>
    <div class="rule-set">
      <span class="rule-blue" style="left:0;width:100px"></span>
      <span class="rule-orange" style="left:124px;width:180px"></span>
      <span class="rule-green" style="left:328px;width:116px"></span>
    </div>
    <div class="contact">
      418 Hollister Avenue | Suite 500 | New York, NY 10012<br>
      Cell: 917-555-0142 | Fax: 917-555-0143 | Email: Dpruett@brimlow.com | www.mistvaleloft.com
    </div>
  </section>

  <!-- Business card front -->
  <section class="piece card-front">
    <div class="brand">
      <div class="brand-dot"></div>
      <div class="brand-name">MISTVALE</div>
    </div>
    <div class="holder">
      <div class="holder-name">Dale Pruett</div>
      <div class="holder-title">Executive Director</div>
    </div>
    <div class="rule-set">
      <span class="rule-blue" style="left:0;width:60px"></span>
      <span class="rule-orange" style="left:72px;width:76px"></span>
      <span class="rule-green" style="left:160px;width:56px"></span>
    </div>
    <div class="contact">
      418 Hollister Avenue | Suite 500 | New York, NY 10012<br>
      Cell: 917-555-0142 | Dpruett@brimlow.com | www.mistvaleloft.com
    </div>
  </section>

  <!-- Business card back -->
  <section class="piece card-back">
    <div class="brand">
      <div class="brand-dot"></div>
      <div class="brand-name">MISTVALE</div>
    </div>
  </section>
</div>
</body>
</html>
```